Executive Business Consulting for Telco Companies and Telco Start up companies

1.) Looking for an appealing and action oriented business card design.
2.)The target companies to work with start-ups and existing companies that focus on Business to Business applications
3.) For "OKRA", a Belgium based Executive consultancy company specialised in global reach starting from the centre of Europe = Brussels.
4.) Our core competence is the Go To Market in All major global regions, incl North America, Latin America, Asia, Japan, Europe and Africa.
5.) Design should be appealing to CEO, CFO and Venture Funds signalling; Expertise, Stability, Maturity and Commitment
6.) Preferred color scheme is Blue focussed and using a modern FONT.
7.) Logo design is included (uploaded)

Target Market(s)

Telecommunication Market. Companies in a B2B business model, developping services or applications to make business run more profitable

Industry/Entity Type

Business

Contact Information for Business Card

Company Name: OKRA
Name: Joris Vandelay
Titel: Managing Director
Address: Kalkweg 58 , B-9170 Meerdonk , Belgium
Tel: + 32 471 208 364
Email: joris_vandelay@plimbox.example
LinkedIn: be.netprofilo.example/in/jorisvandelay/

Font styles to use
Serif

Colors
0455a3
3277b5

Requirements
Must have
• Second Side Text: Global Market Entry and Growth Execution

```html
<!DOCTYPE html>
<html lang="en">
<head>
<meta charset="utf-8">
<title>OKRA – Business Card</title>
<link rel="stylesheet" href="https://fonts.googleapis.com/css2?family=Ubuntu:wght@400;500;700&display=swap">
<style>
  :root {
    --bg: #2b2b2d;
    --navy: #1c2a78;
    --navy-deep: #15205f;
    --ink: #1a2a6c;
    --brand-blue: #0455a3;
    --accent-blue: #3277b5;
    --sky: #2a9ad6;
    --silver: #c4c8cc;
    --arc-grey: #c9cbcd;
    --paper-light: #ffffff;
    --paper-shade: #e4e5e7;
    --text: #243063;
  }
  * { box-sizing: border-box; margin: 0; padding: 0; }
  html, body { width: 1200px; height: 900px; overflow: hidden; }
  body {
    background: var(--bg);
    font-family: "Ubuntu", sans-serif;
    position: relative;
  }
  .card {
    position: absolute;
    width: 620px;
    height: 354px;
    border-radius: 22px;
    overflow: hidden;
  }

  /* Back side */
  .card-back {
    left: 80px;
    top: 90px;
    background: linear-gradient(160deg, var(--navy) 0%, var(--navy-deep) 100%);
  }
  .card-back .wordmark {
    position: absolute;
    left: 0; right: 0;
    top: 132px;
    text-align: center;
    font-weight: 700;
    font-size: 108px;
    letter-spacing: 6px;
    color: var(--silver);
    line-height: 1;
  }
  .card-back .tagline {
    position: absolute;
    left: 0; right: 0;
    top: 252px;
    text-align: center;
    font-size: 17px;
    letter-spacing: 0.5px;
    color: var(--sky);
  }

  /* Front side */
  .card-front {
    left: 500px;
    top: 456px;
    background: linear-gradient(120deg, var(--paper-light) 30%, var(--paper-shade) 100%);
  }
  .card-front .decor {
    position: absolute;
    inset: 0;
  }
  .card-front .wordmark {
    position: absolute;
    left: 320px;
    top: 40px;
    font-weight: 700;
    font-size: 46px;
    letter-spacing: 3px;
    color: var(--ink);
    line-height: 1;
  }
  .contact {
    position: absolute;
    left: 320px;
    top: 126px;
    color: var(--text);
  }
  .contact .name {
    font-size: 21px;
    font-weight: 500;
    color: var(--sky);
  }
  .contact .role {
    font-size: 14px;
    margin-top: 3px;
    margin-bottom: 12px;
  }
  .contact-list { list-style: none; }
  .contact-list li {
    display: flex;
    align-items: flex-start;
    gap: 8px;
    font-size: 14px;
    line-height: 21px;
  }
  .contact-list .icon {
    width: 13px; height: 13px;
    margin-top: 4px;
    flex: none;
    fill: var(--brand-blue);
  }
</style>
</head>
<body>

<section class="card card-back" aria-label="Business card back">
  <div class="wordmark">OKRA</div>
  <div class="tagline">Global Market Entry and Growth Execution</div>
</section>

<section class="card card-front" aria-label="Business card front">
  <svg class="decor" viewBox="0 0 620 354" width="620" height="354">
    <defs>
      <linearGradient id="globeFill" x1="0" y1="0" x2="1" y2="1">
        <stop offset="0" stop-color="#3aa7de"/>
        <stop offset="1" stop-color="#0455a3"/>
      </linearGradient>
    </defs>
    <path role="img" aria-label="Brand globe graphic" d="M0 0 H150 A280 280 0 0 1 0 354 Z" fill="url(#globeFill)" opacity="0.85"/>
    <path d="M200 0 A320 320 0 0 1 10 354" fill="none" stroke="var(--arc-grey)" stroke-width="20"/>
  </svg>

  <div class="wordmark">OKRA</div>

  <div class="contact">
    <div class="name">Joris Vandelay</div>
    <div class="role">Managing Director</div>
    <ul class="contact-list">
      <li>
        <svg class="icon" viewBox="0 0 16 16"><path d="M3.5 1.5l2.5 3-1.5 1.8a9 9 0 0 0 5.2 5.2l1.8-1.5 3 2.5-1.6 2A12 12 0 0 1 1.5 3.1z"/></svg>
        <span>+ 32 471 208 364</span>
      </li>
      <li>
        <svg class="icon" viewBox="0 0 16 16"><path d="M1 3h14v10H1z M2 4l6 5 6-5" stroke="#fff" stroke-width="1"/></svg>
        <span>joris_vandelay@plimbox.example</span>
      </li>
      <li>
        <svg class="icon" viewBox="0 0 16 16"><rect x="1" y="1" width="14" height="14" rx="2"/></svg>
        <span>be.netprofilo.example/in/jorisvandelay/</span>
      </li>
      <li>
        <svg class="icon" viewBox="0 0 16 16"><path d="M8 1a5 5 0 0 1 5 5c0 4-5 9-5 9S3 10 3 6a5 5 0 0 1 5-5zm0 3a2 2 0 1 0 0 4 2 2 0 0 0 0-4z"/></svg>
        <span>Kalkweg 58, B-9170 Meerdonk<br>Belgium</span>
      </li>
    </ul>
  </div>
</section>

</body>
</html>
```